Door Hanger Design for Electricians Serving Homes

I would like our logo incorporated into the door hanger. We would like a place for a tear off section on the bottom of the hanger with our contact information: K&T Electric - (555) 318-4702 - www.kandtelectric.example - info@kandtelectric.example.
Door Hanger Script
Front Side of the Door Hanger:
[Company Logo]
Need a Reliable Electrician?
Your Local Electrical Expert is Just Around the Corner!
• Quick Response Times
• Affordable Rates
• Quality Workmanship
• Fully Licensed & Insured
• Special Offer:
• 10% OFF Your First Service Call!
Back Side of the Door Hanger:
Don't Let Electrical Issues Keep You in the Dark!
From flickering lights to complete system upgrades, we've got all your
residential electrical needs covered. Our services include:
• Electrical Repairs & Troubleshooting
• Lighting Installation & Upgrades
• Safety Inspections & Code Compliance
• Energy-Efficient Solutions
• 24/7 Emergency Services
• Why Choose Us?
• Friendly, Local Service
• Over 30 Years of Experience
• Satisfaction Guaranteed
• Upfront Pricing
Call Us Today: [Your Phone Number]
Visit Our Website: [Your Website]
Book Your Appointment Now and Claim Your 10% Discount!
Offer valid for new customers on the first visit only. Mention this door hanger when
booking.
[Your Company Name and Contact Information]
Follow Us on Social Media for More Tips and Special Offers!
[Icons for social media platforms: Chatterpage, Pixmosaic, Quibbler, etc.]
Design Tips:
Use bold, clear fonts for easy reading.
Incorporate your brand colors and logo for instant recognition.
Include a clear call to action (CTA) on both sides.
Add a tear-off section at the bottom with your contact information for
convenience.
Use high-quality images or graphics related to electrical work to catch
the eye.
This door hanger design and copy aim to attract residential clients by
highlighting the benefits of your electrical services, special offers, and
how they can easily get in touch with you for their electrical needs.
The door knocker template will have three of the same design on front and three of the same design on the back. This template is from the print shop.

```html
<!DOCTYPE html>
<html lang="en">
<head>
<meta charset="utf-8">
<title>K&amp;T Electric – Door Hanger</title>
<link rel="stylesheet" href="https://fonts.googleapis.com/css2?family=Bebas+Neue&family=Oswald:wght@300&family=Poppins:wght@400;600;700;800&display=swap">
<style>
  :root {
    --stage: #808080;
    --red: #ed1c24;
    --red-deep: #a8121b;
    --black: #0b0b0b;
    --ink: #1e1e1e;
    --white: #ffffff;
    --panel: #e6e6e8;
  }
  html, body { margin: 0; padding: 0; }
  body {
    width: 1200px; height: 1117px; overflow: hidden;
    background: var(--stage);
    position: relative;
  }
  .hanger { position: absolute; top: 46px; width: 445px; height: 1025px; display: block; }
  .hanger--front { left: 151px; }
  .hanger--back { left: 638px; }
  .display { font-family: "Bebas Neue", "Oswald", sans-serif; }
  .display-light { font-family: "Oswald", sans-serif; font-weight: 300; }
  .body { font-family: "Poppins", sans-serif; }
  .w4 { font-weight: 400; } .w6 { font-weight: 600; } .w7 { font-weight: 700; } .w8 { font-weight: 800; }
  .fill-white { fill: var(--white); } .fill-red { fill: var(--red); }
  .fill-ink { fill: var(--ink); } .fill-black { fill: var(--black); }
</style>
</head>
<body>

<!-- Front side -->
<svg class="hanger hanger--front" viewBox="0 0 736 1698" xmlns="http://www.w3.org/2000/svg">
  <defs>
    <linearGradient id="photoKitchen" x1="0" y1="0" x2="1" y2="1">
      <stop offset="0" stop-color="#c9ccd0"/>
      <stop offset="0.5" stop-color="#8d8f93"/>
      <stop offset="1" stop-color="#5a4234"/>
    </linearGradient>
    <linearGradient id="photoPanel" x1="0" y1="0" x2="1" y2="1">
      <stop offset="0" stop-color="#c3c6cc"/>
      <stop offset="0.45" stop-color="#4b4e57"/>
      <stop offset="1" stop-color="#d8d3bf"/>
    </linearGradient>
    <linearGradient id="redBand" x1="0" y1="0" x2="1" y2="1">
      <stop offset="0" stop-color="#d0161e"/>
      <stop offset="0.4" stop-color="#ed1c24"/>
      <stop offset="1" stop-color="#a8121b"/>
    </linearGradient>
    <linearGradient id="stripeShine" x1="0" y1="0" x2="1" y2="0">
      <stop offset="0" stop-color="#0b0b0b"/>
      <stop offset="0.25" stop-color="#8a8a8a"/>
      <stop offset="0.45" stop-color="#0b0b0b"/>
      <stop offset="1" stop-color="#0b0b0b"/>
    </linearGradient>
    <symbol id="tick" viewBox="0 0 20 20">
      <circle cx="10" cy="10" r="10" fill="#ed1c24"/>
      <path d="M5.5 10.3 L8.6 13.3 L14.6 7" fill="none" stroke="#fff" stroke-width="2.6" stroke-linecap="round" stroke-linejoin="round"/>
    </symbol>
    <symbol id="iconPhone" viewBox="0 0 24 24">
      <circle cx="12" cy="12" r="12" fill="#ed1c24"/>
      <path d="M8 6.5 C7 7.5 6.8 9.5 8.8 12.2 C10.8 14.9 13.6 17.2 15.6 17 L17.3 15.4 L14.9 13.4 L13.6 14.3 C12.4 13.7 10.4 11.7 9.8 10.4 L10.7 9.1 Z" fill="#fff"/>
    </symbol>
    <symbol id="iconMail" viewBox="0 0 24 24">
      <circle cx="12" cy="12" r="12" fill="#ed1c24"/>
      <rect x="6.5" y="8" width="11" height="8" fill="none" stroke="#fff" stroke-width="1.4"/>
      <path d="M6.5 8 L12 12.5 L17.5 8" fill="none" stroke="#fff" stroke-width="1.4"/>
    </symbol>
    <symbol id="iconGlobe" viewBox="0 0 24 24">
      <circle cx="12" cy="12" r="12" fill="#ed1c24"/>
      <circle cx="12" cy="12" r="6" fill="none" stroke="#fff" stroke-width="1.4"/>
      <ellipse cx="12" cy="12" rx="2.6" ry="6" fill="none" stroke="#fff" stroke-width="1.2"/>
      <path d="M6 12 H18" stroke="#fff" stroke-width="1.2"/>
    </symbol>
  </defs>

  <rect class="fill-white" width="736" height="1698"/>

  <g class="hero">
    <polygon points="0,0 736,0 736,620 540,672 0,613" fill="url(#photoKitchen)" role="img" aria-label="Photo of a bright modern kitchen and dining area with pendant lights"/>
    <polygon points="461,0 736,0 736,263 509,193" fill="#fff"/>
    <g class="logo">
      <text x="612" y="150" text-anchor="middle" class="body w8 fill-black" font-size="78">K&amp;T</text>
      <text x="612" y="192" text-anchor="middle" class="body w8 fill-black" font-size="26">ELECTRIC, LLC</text>
    </g>
    <circle class="hanger-hole" cx="365" cy="223" r="100" fill="#808080"/>
  </g>

  <polygon class="stripe" points="0,643 736,718 736,748 0,673" fill="url(#stripeShine)"/>

  <g class="headline-band">
    <polygon points="0,685 736,763 736,1018 0,943" fill="url(#redBand)"/>
    <text x="367" y="808" text-anchor="middle" class="display-light fill-white" font-size="40">NEED A RELIABLE ELECTRICIAN?</text>
    <text x="367" y="868" text-anchor="middle" class="display fill-white" font-size="66">YOUR LOCAL ELECTRICAL EXPERT IS</text>
    <text x="367" y="928" text-anchor="middle" class="display fill-white" font-size="66">JUST AROUND THE CORNER!</text>
  </g>

  <g class="benefits">
    <path d="M82 1075 V998 H157" fill="none" stroke="#ed1c24" stroke-width="3"/>
    <path d="M82 1088 V1130" fill="none" stroke="#ed1c24" stroke-width="3" stroke-dasharray="10 8"/>
    <use href="#tick" x="132" y="1048" width="26" height="26"/>
    <text x="177" y="1073" class="body w4 fill-ink" font-size="37">Quick Response Times</text>
    <use href="#tick" x="132" y="1096" width="26" height="26"/>
    <text x="177" y="1121" class="body w4 fill-ink" font-size="37">Affordable Rates</text>
    <use href="#tick" x="132" y="1144" width="26" height="26"/>
    <text x="177" y="1169" class="body w4 fill-ink" font-size="37">Quality Workmanship</text>
    <use href="#tick" x="132" y="1192" width="26" height="26"/>
    <text x="177" y="1217" class="body w4 fill-ink" font-size="37">Fully Licensed &amp; Insured</text>
  </g>

  <g class="offer">
    <polygon points="224,1280 236,1268 517,1268 505,1325 224,1325" fill="#ed1c24"/>
    <text x="367" y="1311" text-anchor="middle" class="body w7 fill-white" font-size="34">Special Offer:</text>
    <rect x="224" y="1325" width="432" height="66" rx="8" fill="none" stroke="#ed1c24" stroke-width="3"/>
    <text x="246" y="1372" class="body w7 fill-black" font-size="33">Your First Service Call!</text>
    <rect x="72" y="1322" width="150" height="72" fill="#fff"/>
    <text x="74" y="1390" class="body w8 fill-black" font-size="92" letter-spacing="-4">10</text>
    <text x="170" y="1362" class="body w7 fill-black" font-size="50">%</text>
    <text x="170" y="1390" class="body w8 fill-black" font-size="24">OFF</text>
  </g>

  <g class="tear-off">
    <polygon points="0,1418 232,1476 0,1495" fill="#ed1c24"/>
    <polygon points="0,1508 736,1456 736,1698 0,1698" fill="#0b0b0b"/>
    <line x1="0" y1="1516" x2="736" y2="1516" stroke="#fff" stroke-width="2" stroke-dasharray="10 7"/>
    <text x="106" y="1596" class="body w7 fill-white" font-size="25">K&amp;T Electric</text>
    <use href="#iconPhone" x="72" y="1614" width="24" height="24"/>
    <text x="106" y="1636" class="body w4 fill-white" font-size="24">(555) 318-4702</text>
    <use href="#iconMail" x="310" y="1572" width="24" height="24"/>
    <text x="344" y="1592" class="body w4 fill-white" font-size="23">www.kandtelectric.example</text>
    <use href="#iconGlobe" x="310" y="1614" width="24" height="24"/>
    <text x="344" y="1636" class="body w4 fill-white" font-size="23">info@kandtelectric.example</text>
  </g>
</svg>

<!-- Back side -->
<svg class="hanger hanger--back" viewBox="0 0 736 1698" xmlns="http://www.w3.org/2000/svg">
  <rect class="fill-white" width="736" height="1698"/>

  <g class="hero">
    <polygon points="0,0 736,0 736,323 560,374 0,318" fill="url(#photoPanel)" role="img" aria-label="Photo of a gloved electrician working on wires in a breaker panel"/>
    <circle class="hanger-hole" cx="365" cy="223" r="100" fill="#808080"/>
  </g>

  <polygon class="stripe" points="0,343 736,418 736,448 0,373" fill="url(#stripeShine)"/>

  <g class="headline-band">
    <polygon points="0,388 736,468 736,758 0,713" fill="url(#redBand)"/>
    <text x="368" y="525" text-anchor="middle" class="display fill-white" font-size="64">DON'T LET ELECTRICAL ISSUES</text>
    <text x="368" y="585" text-anchor="middle" class="display fill-white" font-size="64">KEEP YOU IN THE DARK!</text>
    <text x="368" y="623" text-anchor="middle" class="display fill-white" font-size="32">FROM FLICKERING LIGHTS TO COMPLETE SYSTEM UPGRADES,</text>
    <text x="368" y="655" text-anchor="middle" class="display fill-white" font-size="32">WE'VE GOT ALL YOUR RESIDENTIAL ELECTRICAL</text>
    <text x="368" y="685" text-anchor="middle" class="display fill-white" font-size="32">NEEDS COVERED.</text>
  </g>

  <polygon class="why-panel" points="368,735 736,758 736,1095 368,1058" fill="#e6e6e8"/>

  <g class="services">
    <path d="M30 790 V728 H86" fill="none" stroke="#ed1c24" stroke-width="3"/>
    <path d="M30 800 V830" fill="none" stroke="#ed1c24" stroke-width="3" stroke-dasharray="6 6"/>
    <text x="63" y="793" class="display fill-black" font-size="32"><tspan class="fill-red">OUR SERVICES</tspan> INCLUDE</text>
    <use href="#tick" x="63" y="817" width="15" height="15"/>
    <text x="93" y="831" class="body w4 fill-ink" font-size="20">Electrical Repairs &amp;</text>
    <text x="93" y="853" class="body w4 fill-ink" font-size="20">Troubleshooting</text>
    <use href="#tick" x="63" y="884" width="15" height="15"/>
    <text x="93" y="898" class="body w4 fill-ink" font-size="20">Lighting Installation &amp;</text>
    <text x="93" y="920" class="body w4 fill-ink" font-size="20">Upgrades</text>
    <use href="#tick" x="63" y="950" width="15" height="15"/>
    <text x="93" y="964" class="body w4 fill-ink" font-size="20">Safety Inspections &amp;</text>
    <text x="93" y="986" class="body w4 fill-ink" font-size="20">Code Compliance</text>
    <use href="#tick" x="63" y="1017" width="15" height="15"/>
    <text x="93" y="1031" class="body w4 fill-ink" font-size="20">Energy-Efficient Solutions</text>
    <use href="#tick" x="63" y="1062" width="15" height="15"/>
    <text x="93" y="1076" class="body w4 fill-ink" font-size="20">24/7 Emergency Services</text>
  </g>

  <g class="why-us">
    <text x="399" y="798" class="display fill-black" font-size="32"><tspan class="fill-red">WHY</tspan> CHOOSE US</text>
    <use href="#tick" x="399" y="821" width="15" height="15"/>
    <text x="426" y="835" class="body w4 fill-ink" font-size="20">Friendly, Local Service</text>
    <use href="#tick" x="399" y="869" width="15" height="15"/>
    <text x="426" y="883" class="body w4 fill-ink" font-size="20">Over 30 Years of</text>
    <text x="426" y="907" class="body w4 fill-ink" font-size="20">Experience</text>
    <use href="#tick" x="399" y="941" width="15" height="15"/>
    <text x="426" y="955" class="body w4 fill-ink" font-size="20">Satisfaction</text>
    <text x="426" y="979" class="body w4 fill-ink" font-size="20">Guaranteed</text>
    <use href="#tick" x="399" y="1013" width="15" height="15"/>
    <text x="426" y="1027" class="body w4 fill-ink" font-size="20">Upfront Pricing</text>
  </g>

  <g class="contact-box">
    <path d="M178 1191 H75 Q65 1191 65 1181 V1133 Q65 1123 75 1123 H661 Q671 1123 671 1133 V1181 Q671 1191 661 1191 H556" fill="none" stroke="#ed1c24" stroke-width="3"/>
    <text x="368" y="1161" text-anchor="middle" class="body w4 fill-ink" font-size="18">Visit Our Website: <tspan class="w7 fill-black" font-size="23">www.kandtelectric.example</tspan></text>
    <text x="368" y="1199" text-anchor="middle" class="body w4 fill-ink" font-size="18">Call Us Today: <tspan class="w7 fill-black" font-size="27">(555) 318-4702</tspan></text>
  </g>

  <g class="cta">
    <rect x="66" y="1231" width="604" height="152" rx="18" fill="#0b0b0b"/>
    <text x="368" y="1275" text-anchor="middle" class="body w7 fill-white" font-size="27">Book Your Appointment Now and Claim</text>
    <text x="368" y="1305" text-anchor="middle" class="body w7 fill-white" font-size="27">Your <tspan class="fill-red">10% Discount!</tspan></text>
    <text x="368" y="1335" text-anchor="middle" class="body w4 fill-white" font-size="19">Offer valid for new customers on the first visit only.</text>
    <text x="368" y="1357" text-anchor="middle" class="body w4 fill-white" font-size="19">Mention this door hanger when booking.</text>
  </g>

  <g class="social">
    <text x="548" y="1420" text-anchor="end" class="body w4 fill-ink" font-size="14">Follow Us on Social Media for More Tips and Special Offers!</text>
    <circle cx="568" cy="1414" r="7" fill="#ed1c24" aria-label="Chatterpage"/>
    <circle cx="586" cy="1414" r="7" fill="#ed1c24" aria-label="Quibbler"/>
    <circle cx="604" cy="1414" r="7" fill="#ed1c24" aria-label="Pixmosaic"/>
  </g>

  <g class="tear-off">
    <polygon points="0,1418 232,1476 0,1495" fill="#ed1c24"/>
    <polygon points="0,1508 736,1456 736,1698 0,1698" fill="#0b0b0b"/>
    <line x1="0" y1="1516" x2="736" y2="1516" stroke="#fff" stroke-width="2" stroke-dasharray="10 7"/>
    <text x="106" y="1596" class="body w7 fill-white" font-size="25">K&amp;T Electric</text>
    <use href="#iconPhone" x="72" y="1614" width="24" height="24"/>
    <text x="106" y="1636" class="body w4 fill-white" font-size="24">(555) 318-4702</text>
    <use href="#iconMail" x="310" y="1572" width="24" height="24"/>
    <text x="344" y="1592" class="body w4 fill-white" font-size="23">www.kandtelectric.example</text>
    <use href="#iconGlobe" x="310" y="1614" width="24" height="24"/>
    <text x="344" y="1636" class="body w4 fill-white" font-size="23">info@kandtelectric.example</text>
  </g>
</svg>

</body>
</html>
```